Flyer for Golden Hearth Catering Company

Flyer Size: Double Sided 210mm * 148mm (Half a Sheet of Paper)
For your reference I have attached the logo and the web address is www.goldenhearthcatering.example.
Specifications:
- Must contain the menu pricing chart, contact information, and hours of operation posted on the website.
- The menu must have an organization system from 1. Select Glaze through 4.Drinks. This will be the determining factor for selection. Graphic must be a mixture of creativity and function.
-The flyer can be identical on both sides (Not a determining factor)
-Incorporate the logo on both sides.
-The flyer does not have to be based on the website. (Not a determining factor)
My team will be handing these flyers out to HR Directors and Securities at Corporate offices.
Please let me know if you have any questions.
Updates
Project Deadline Extended
Reason: Website was not operational .
Brief has been updated and the website is up for your reference.
Target Market(s)
Corporate Office Catering. Secretary or HR director, usually a female.
Industry/Entity Type
Catering
Look and feel
Each slider illustrates characteristics of the customer's brand and the style your logo design should communicate.

```html
<!DOCTYPE html>
<html lang="en">
<head>
<meta charset="utf-8">
<title>Golden Hearth Catering Flyer</title>
<link href="https://fonts.googleapis.com/css2?family=Alfa+Slab+One&family=Arvo:wght@700&display=swap" rel="stylesheet">
<style>
  :root {
    --page: #e9e6e1;
    --board: #232323;
    --board-light: #3a3a3a;
    --gold: #fbb40a;
    --gold-text: #f7b500;
    --red: #b3200f;
    --orange: #ef3a12;
    --white: #ffffff;
    --ink: #1a1a1a;
  }
  * { box-sizing: border-box; margin: 0; padding: 0; }
  html, body { width: 1200px; height: 675px; overflow: hidden; background: var(--page); }
  .canvas { position: relative; width: 1200px; height: 675px; }
  .flyer {
    position: absolute; top: 135px; width: 570px; height: 404px; overflow: hidden;
    background: radial-gradient(ellipse at 55% 45%, var(--board-light) 0%, var(--board) 70%);
    box-shadow: 0 6px 14px rgba(0,0,0,.35);
    font-family: "Arvo", Georgia, serif;
  }
  .flyer--menu { left: 30px; }
  .flyer--pricing { left: 600px; }

  .flames {
    position: absolute; top: 0; left: 150px; width: 170px; height: 140px;
    background: radial-gradient(ellipse at 40% 60%, rgba(255,170,20,.85) 0%, rgba(240,90,10,.45) 45%, rgba(35,35,35,0) 75%);
  }
  .brand {
    position: absolute; top: 0; left: 0; width: 262px; height: 105px;
    background: var(--white);
    clip-path: polygon(0 0, 100% 0, 100% 76%, 0 100%);
    display: flex; align-items: center; gap: 10px; padding: 0 14px 16px 14px;
  }
  .brand__mark { width: 40px; height: 40px; border-radius: 50%; background: var(--orange); flex: none; }
  .brand__name { font-size: 17px; line-height: 1.15; color: var(--orange); font-weight: 700; }

  .panel { position: absolute; background: var(--gold); }
  .panel--glaze { left: 26px; top: 110px; width: 240px; height: 294px; border-radius: 0 26px 0 0; padding: 18px 14px 0 16px; }
  .panel--extras { left: 313px; top: 0; width: 240px; height: 357px; border-radius: 0 0 24px 24px; padding: 28px 14px 0 22px; }

  .section-title {
    font-family: "Alfa Slab One", Georgia, serif; font-size: 12.5px; line-height: 1.1;
    color: var(--red); text-transform: uppercase; letter-spacing: .2px;
  }
  .panel--glaze .section-title { text-align: right; margin-bottom: 10px; }
  .panel--extras .section-title { margin-bottom: 3px; margin-left: -8px; }
  .item-list { list-style: none; color: var(--white); font-size: 10px; line-height: 14.4px; text-transform: uppercase; letter-spacing: .3px; }
  .panel--extras .item-list { margin-bottom: 19px; }

  .dish {
    position: absolute; right: 0; bottom: 0; width: 130px; height: 62px;
    border-radius: 40px 0 0 0;
    background: radial-gradient(ellipse at 60% 60%, #9a5a24 0%, #6e3812 55%, #f1ece4 80%);
  }

  .pricing { position: absolute; left: 18px; top: 170px; }
  .pricing__labels { position: absolute; left: 0; top: 8px; color: var(--white); font-size: 11px; line-height: 28px; white-space: nowrap; }
  .pricing__grid { position: absolute; left: 86px; top: 0; display: flex; gap: 4.7px; }
  .price-cell {
    width: 39px; height: 58px; background: var(--gold); color: var(--white);
    display: flex; flex-direction: column; align-items: center; justify-content: space-around;
    font-size: 10.5px; padding: 6px 0;
  }
  .price-cell__price { font-style: italic; font-size: 10px; }

  .contact { position: absolute; left: 0; width: 100%; padding-left: 40px; top: 272px; text-align: center; }
  .contact__title { font-family: "Alfa Slab One", Georgia, serif; color: var(--gold-text); font-size: 19px; font-weight: 400; }
  .contact__line { color: var(--white); font-size: 13px; line-height: 18px; }
  .contact__web { position: absolute; left: 0; width: 100%; padding-left: 40px; top: 373px; text-align: center; color: var(--gold-text); font-size: 12px; }
</style>
</head>
<body>
<main class="canvas">

  <section class="flyer flyer--menu">
    <div class="flames" role="img" aria-label="Flames and red and green chili peppers"></div>
    <header class="brand">
      <span class="brand__mark"></span>
      <span class="brand__name">Golden Hearth<br>Catering</span>
    </header>

    <div class="panel panel--glaze">
      <h2 class="section-title">Select Rotisserie<br>Chicken Glaze</h2>
      <ul class="item-list">
        <li>Original</li><li>Barbecue</li><li>Honey</li><li>Spicy</li><li>Chipotle</li>
        <li>Chipotle-Lime</li><li>Jamaican Jerk</li><li>Teriyaki</li><li>Buffalo</li>
        <li>Balsamic Chicken</li><li>Hawaiian</li><li>Lemon Pepper Rosemary</li>
        <li>Lemonade Chicken</li><li>Lemon Zest</li><li>Orange</li><li>Orange and Onion</li>
      </ul>
    </div>

    <div class="panel panel--extras">
      <h2 class="section-title">Select Sides</h2>
      <ul class="item-list">
        <li>Caesar Salad</li><li>Fried Rice</li><li>White Rice</li><li>Mashed Potatoes</li><li>Hummus &amp; Pita</li>
      </ul>
      <h2 class="section-title">Select Dessert</h2>
      <ul class="item-list">
        <li>Hazelnut Spread Covered Chocolate</li><li>Chip Cookies</li>
      </ul>
      <h2 class="section-title">Select Drinks</h2>
      <ul class="item-list">
        <li>Cola</li><li>Diet Cola</li><li>Lemon-Lime Soda</li>
        <li>Brewed Ice Tea (Iced Tea &amp;</li><li>Lemon Tea)</li><li>Spring Water</li>
      </ul>
    </div>

    <div class="dish" role="img" aria-label="Plate of roasted rotisserie chicken with flames"></div>
  </section>

  <section class="flyer flyer--pricing">
    <div class="flames" role="img" aria-label="Flames and red and green chili peppers"></div>
    <header class="brand">
      <span class="brand__mark"></span>
      <span class="brand__name">Golden Hearth<br>Catering</span>
    </header>

    <div class="pricing">
      <div class="pricing__labels">PARTY SIZE:<br>PRICE:</div>
      <div class="pricing__grid">
        <div class="price-cell"><span>10</span><span class="price-cell__price">$105</span></div>
        <div class="price-cell"><span>20</span><span class="price-cell__price">$165</span></div>
        <div class="price-cell"><span>30</span><span class="price-cell__price">$225</span></div>
        <div class="price-cell"><span>40</span><span class="price-cell__price">$290</span></div>
        <div class="price-cell"><span>50</span><span class="price-cell__price">$330</span></div>
        <div class="price-cell"><span>60</span><span class="price-cell__price">$395</span></div>
        <div class="price-cell"><span>80</span><span class="price-cell__price">$515</span></div>
        <div class="price-cell"><span>100</span><span class="price-cell__price">$625</span></div>
        <div class="price-cell"><span>150</span><span class="price-cell__price">$940</span></div>
        <div class="price-cell"><span>200</span><span class="price-cell__price">$1,235</span></div>
      </div>
    </div>

    <div class="contact">
      <h2 class="contact__title">CONTACT US</h2>
      <p class="contact__line">(555) 014-2290</p>
      <p class="contact__line">SALES@GOLDENHEARTHCATERING.EXAMPLE</p>
    </div>
    <p class="contact__web">www.goldenhearthcatering.example</p>

    <div class="dish" role="img" aria-label="Plate of roasted rotisserie chicken with flames"></div>
  </section>

</main>
</body>
</html>
```